QuadLantern--Help Us look fresh and new to companies, college students and college career centers!

We just designed a new logo and would like to freshen-up and make our business cards a bit more modern. Not crazy-modern like Picasso, but modern like metro-style and fresh like fruit. We use three logos with a combination of two colors each, and three colors total. We are looking for a single format to apply to three different cards/color schemes (green/blue to give out to companies, orange/green for students, and orange/blue for university career centers). Thanks everyone--looking forward to seeing your designs!!

Target Market(s)

Three styles: companies, college students/grads, college career centers

Industry/Entity Type

College

Contact Information for Business Card

Address: 1187 9th Avenue, Suite 614, Seattle, WA 98104. Need a spot for email address, web address (www.quadlantern-example.com), and phone numbers (main, direct, mobile). Don't open that website unless you want to lose your lunch--it is waaaay old and outdated. See this link instead, http://staging.brixelworks-example.com/QuadLantern/EmployerSolutions, for our new website design in progress.

Font styles to use
Sans Serif

Requirements
Must have
• Please use the logos supplied. Would like text to be grey but printable, like a "light" type style that is metro-type with sans-serif. NOT black text. Modern. For inspiration, here's a link to our work-in-progress website we are planning to launch soon: http://staging.brixelworks-example.com/QuadLantern/EmployerSolutions
Nice to have
• Would like to see something unique and different in a "metro" style. Clean and not cluttered.
Should not have
• No odd-sized cards

```html
<!DOCTYPE html>
<html lang="en">
<head>
<meta charset="utf-8">
<title>QuadLantern business card</title>
<link href="https://fonts.googleapis.com/css2?family=Lato:wght@300;400;700;900&display=swap" rel="stylesheet">
<style>
  :root {
    --bg: #2a2a2c;
    --card: #ffffff;
    --blue: #0a79b8;
    --orange: #e2921f;
    --white: #ffffff;
  }
  html, body {
    margin: 0; padding: 0;
    width: 1200px; height: 873px;
    overflow: hidden;
    background: var(--bg);
    font-family: "Lato", sans-serif;
  }
  .stage {
    position: relative;
    width: 1200px; height: 873px;
    display: flex; align-items: center; justify-content: center; gap: 40px;
  }
  .card {
    position: relative;
    width: 540px; height: 309px;
    background: var(--card);
    border-radius: 14px;
    overflow: hidden;
    box-shadow: 0 10px 30px rgba(0,0,0,.45);
  }
  /* Front */
  .front-name {
    position: absolute;
    right: 34px; top: 118px;
    font-weight: 900; font-size: 34px;
    color: var(--orange);
    letter-spacing: -.5px;
  }
  /* Back */
  .brand {
    position: absolute; left: 0; right: 0; top: 0; height: 125px;
    display: flex; align-items: center; justify-content: center; gap: 12px;
  }
  .brand-dot {
    width: 30px; height: 30px; border-radius: 50%;
    background: var(--blue);
  }
  .brand-name {
    font-weight: 900; font-size: 38px; color: var(--orange);
    letter-spacing: -.5px;
  }
  .band {
    position: absolute; left: 0; right: 0; top: 125px; height: 125px;
    display: flex;
  }
  .holder {
    position: relative;
    width: 272px; flex: none;
    background: var(--blue);
    color: var(--white);
  }
  .holder-notch {
    position: absolute; left: 140px; top: 0;
    width: 0; height: 0;
    border-left: 12px solid transparent; border-right: 12px solid transparent;
    border-top: 12px solid var(--card);
  }
  .holder-pointer {
    position: absolute; right: -12px; top: 20px; z-index: 2;
    width: 0; height: 0;
    border-top: 12px solid transparent; border-bottom: 12px solid transparent;
    border-left: 12px solid var(--blue);
  }
  .holder-name {
    position: absolute; left: 28px; top: 52px;
    margin: 0; font-weight: 900; font-size: 28px; white-space: nowrap;
  }
  .holder-title {
    position: absolute; left: 70px; top: 88px;
    margin: 0; font-weight: 400; font-size: 16px;
  }
  .contact {
    flex: 1; background: var(--orange);
    list-style: none; margin: 0;
    padding: 24px 0 0 30px;
    color: var(--white);
    font-size: 12px; font-weight: 400; line-height: 15.5px;
    white-space: nowrap;
  }
  .contact li { display: flex; align-items: center; gap: 9px; }
  .contact svg { width: 11px; height: 11px; flex: none; fill: none; stroke: var(--white); stroke-width: 1.6; }
  .address {
    position: absolute; left: 0; right: 0; bottom: 0; height: 59px;
    display: flex; align-items: center; justify-content: center;
    margin: 0; font-weight: 900; font-size: 14px; color: var(--blue);
  }
</style>
</head>
<body>
<main class="stage">
  <section class="card card-front" aria-label="Card front">
    <div class="front-name">QuadLantern</div>
  </section>

  <section class="card card-back" aria-label="Card back">
    <header class="brand">
      <span class="brand-dot"></span>
      <span class="brand-name">QuadLantern</span>
    </header>
    <div class="band">
      <div class="holder">
        <span class="holder-notch"></span>
        <span class="holder-pointer"></span>
        <p class="holder-name">L Hartwell</p>
        <p class="holder-title">Founder</p>
      </div>
      <ul class="contact">
        <li><svg viewBox="0 0 12 12"><path d="M2 1h3l1 3-2 1a7 7 0 0 0 3 3l1-2 3 1v3c-6 0-9-3-9-9z"/></svg>+31 20 555 0142</li>
        <li><svg viewBox="0 0 12 12"><rect x="3" y="1" width="6" height="10" rx="1"/></svg>+31 27 555 0187</li>
        <li><svg viewBox="0 0 12 12"><rect x="1" y="5" width="10" height="5"/><rect x="3" y="1" width="6" height="4"/></svg>+31 24 555 0163</li>
        <li><svg viewBox="0 0 12 12"><rect x="1" y="2.5" width="10" height="7"/><path d="M1 2.5l5 4 5-4"/></svg>nora@quadlantern-example.com</li>
        <li><svg viewBox="0 0 12 12"><circle cx="6" cy="6" r="5"/><path d="M1 6h10M6 1c-3 3-3 7 0 10M6 1c3 3 3 7 0 10"/></svg>www.quadlantern-example.com</li>
      </ul>
    </div>
    <p class="address">1187 9th Avenue, Suite 614, Seattle, WA 98104</p>
  </section>
</main>
</body>
</html>
```